Note/Card sent to show appreciation to partners who worked with us to improve local communities

I'd like a simple note/card designed for a wide audience. Originally, I called this a "Thanksgiving Card," but it's really just a card to be sent around Thanksgiving, not specifically celebrating the Thanksgiving holiday. We plan to send the card out just prior to Thanksgiving 2017 (Nov. 24, 2017). I work at a regulated electric utility, and we'd like to say thank you to the many stakeholders who we partner with throughout the year to support initiatives that help to improve our state and create opportunities for economic growth. I'm interested mostly in the design of the card, not the simple verbiage on the inside.
Target Market(s)
Customers, charitable foundations, nonprofits, advocacy groups, industry associations, friends

```html
<!DOCTYPE html>
<html lang="en">
<head>
<meta charset="utf-8">
<title>Thanks – A Special Note of Appreciation</title>
<link rel="stylesheet" href="https://fonts.googleapis.com/css2?family=Damion&family=Montserrat:wght@500&display=swap">
<style>
  :root {
    --paper: #fbfaf7;
    --ink-brown: #5b3a1c;
    --ink-soft: #6e4b2c;
    --leaf-orange: #e07a3c;
    --leaf-mustard: #e3ad35;
    --leaf-rust: #b5532f;
    --leaf-olive: #8c9a4a;
    --leaf-brown: #8a5a36;
  }
  html, body {
    margin: 0;
    padding: 0;
    width: 1200px;
    height: 864px;
    overflow: hidden;
    background: var(--paper);
  }
  .card {
    position: relative;
    width: 1200px;
    height: 864px;
    background: var(--paper);
    overflow: hidden;
  }
  .card__wreath {
    position: absolute;
    inset: 0;
    width: 1200px;
    height: 864px;
  }
  .card__message {
    position: absolute;
    left: 0;
    right: 0;
    top: 270px;
    text-align: center;
  }
  .card__headline {
    margin: 0;
    font-family: "Damion", cursive;
    font-weight: 400;
    font-size: 230px;
    line-height: 1;
    color: var(--ink-brown);
    letter-spacing: 2px;
  }
  .card__tagline {
    margin: -14px 0 0;
    font-family: "Montserrat", sans-serif;
    font-weight: 500;
    font-size: 15px;
    letter-spacing: 4px;
    text-transform: uppercase;
    color: var(--ink-soft);
  }
</style>
</head>
<body>
  <main class="card">
    <svg class="card__wreath" viewBox="0 0 1200 864" role="img"
         aria-label="Wreath of scattered autumn leaves, wheat stalks, berry sprigs, acorns and toadstools framing the card">
      <defs>
        <linearGradient id="wreath-tones" x1="0" y1="0" x2="1" y2="1">
          <stop offset="0" stop-color="var(--leaf-mustard)"/>
          <stop offset="0.3" stop-color="var(--leaf-orange)"/>
          <stop offset="0.55" stop-color="var(--leaf-rust)"/>
          <stop offset="0.8" stop-color="var(--leaf-olive)"/>
          <stop offset="1" stop-color="var(--leaf-brown)"/>
        </linearGradient>
        <mask id="wreath-opening">
          <rect width="1200" height="864" fill="#fff"/>
          <ellipse cx="600" cy="420" rx="390" ry="300" fill="#000"/>
        </mask>
      </defs>
      <rect width="1200" height="864" fill="url(#wreath-tones)" opacity="0.55" mask="url(#wreath-opening)"/>
    </svg>

    <section class="card__message">
      <h1 class="card__headline">thanks</h1>
      <p class="card__tagline">A special note of appreciation</p>
    </section>
  </main>
</body>
</html>
```